Sell Velvet Crumb Cheesecake Flyer

I am looking for a designer to help create an attractive sell sheet for my startup company, "Velvet Crumb". We want to build a brand in the cheesecake industry. Velvet Crumb takes a particular approach to preparing one of America’s favorite desserts. Cheesecake is beautiful in nature, so we put a greater emphasis on substance.

Target Market(s)

Lindmoor and Oakhaven County

Industry/Entity Type

It Company

Font styles to use
Sans Serif

Requirements
Must have
• I need the sheet created to include the following:
• Brand Logo, contact info, cheesecake images (not all), types of flavors, build your own options, sizes, prices, delivery availability(local only) and objective statement.I have a web address: www.tryvelvetcrumb.example, but its not active. email address: marna@tryvelvetcrumb.example
Nice to have
• As many images as possible but at least 4 or 5 of my top sellers. Apple, banana, cherry, strawberry shortcake and chocolate.

```html
<!DOCTYPE html>
<html lang="en">
<head>
<meta charset="utf-8">
<title>Velvet Crumb Cheesecake Flyer</title>
<link rel="stylesheet" href="https://fonts.googleapis.com/css2?family=Arimo&family=Open+Sans:wght@700&family=Mulish:wght@400&family=Yesteryear&display=swap">
<style>
  :root {
    --bg-pink: #f2cdd5;
    --bg-pink-light: #f9e3e8;
    --brand-red: #b3293a;
    --body-red: #a8283a;
    --slogan-cream: #fde3a0;
    --banner-cream: #fde9b4;
    --contact-brown: #6b2b2b;
    --frame-brown: #b86a32;
    --frame-peach: #f6d394;
    --frame-lime: #a6cc46;
    --frame-red: #b52430;
    --white: #ffffff;
  }
  html, body { margin: 0; padding: 0; overflow: hidden; }
  body { width: 862px; height: 1200px; }
  .flyer {
    position: relative;
    width: 862px;
    height: 1200px;
    overflow: hidden;
    background: radial-gradient(ellipse at 50% 55%, var(--bg-pink-light) 0%, var(--bg-pink) 65%);
    font-family: "Arimo", Arial, sans-serif;
  }
  .shapes { position: absolute; inset: 0; }
  .brand {
    position: absolute;
    left: 48px;
    top: 110px;
    width: 240px;
    text-align: center;
    font-family: "Mulish", sans-serif;
    font-weight: 400;
    font-size: 50px;
    line-height: 1.15;
    color: var(--brand-red);
    margin: 0;
  }
  .brand-dot {
    display: block;
    width: 26px; height: 26px;
    border-radius: 50%;
    background: var(--brand-red);
    margin: 0 auto 14px;
  }
  .about {
    position: absolute;
    left: 308px;
    top: 70px;
    width: 506px;
    margin: 0;
    font-size: 13.6px;
    line-height: 17.7px;
    text-align: justify;
    color: var(--body-red);
  }
  .slogan {
    position: absolute;
    left: 308px;
    top: 236px;
    width: 520px;
    margin: 0;
    font-family: "Open Sans", sans-serif;
    font-weight: 700;
    font-size: 18px;
    line-height: 20px;
    color: var(--slogan-cream);
  }
  .banner-text {
    position: absolute;
    left: 40px;
    top: 338px;
    width: 700px;
    margin: 0;
    text-align: center;
    font-family: "Yesteryear", cursive;
    font-size: 21px;
    line-height: 30px;
    color: var(--body-red);
    transform: rotate(-6deg);
    transform-origin: center;
  }
  .flavors {
    position: absolute;
    left: 306px;
    top: 441px;
    width: 250px;
    margin: 0;
    padding: 0;
    list-style: none;
    text-align: center;
    font-family: "Mulish", sans-serif;
    font-size: 20px;
    line-height: 27.5px;
    color: var(--brand-red);
  }
  .contact {
    position: absolute;
    left: 0;
    top: 1082px;
    width: 862px;
    margin: 0;
    text-align: center;
    font-family: "Mulish", sans-serif;
    font-size: 30px;
    line-height: 43px;
    letter-spacing: 0.5px;
    color: var(--contact-brown);
  }
  .contact span { display: block; }
</style>
</head>
<body>
<main class="flyer">
  <svg class="shapes" width="862" height="1200" viewBox="0 0 862 1200" aria-hidden="false">
    <defs>
      <polygon id="burst" points="100,0 89.2,11.7 96.6,25.9 83.1,34.4 86.6,50 71.4,54.8 70.7,70.7 54.8,71.4 50,86.6 34.4,83.1 25.9,96.6 11.7,89.2 0,100 -11.7,89.2 -25.9,96.6 -34.4,83.1 -50,86.6 -54.8,71.4 -70.7,70.7 -71.4,54.8 -86.6,50 -83.1,34.4 -96.6,25.9 -89.2,11.7 -100,0 -89.2,-11.7 -96.6,-25.9 -83.1,-34.4 -86.6,-50 -71.4,-54.8 -70.7,-70.7 -54.8,-71.4 -50,-86.6 -34.4,-83.1 -25.9,-96.6 -11.7,-89.2 0,-100 11.7,-89.2 25.9,-96.6 34.4,-83.1 50,-86.6 54.8,-71.4 70.7,-70.7 71.4,-54.8 86.6,-50 83.1,-34.4 96.6,-25.9 89.2,-11.7"/>
      <linearGradient id="banner-fade" x1="0" y1="0" x2="1" y2="0">
        <stop offset="0" stop-color="#fde9b4" stop-opacity="0.75"/>
        <stop offset="1" stop-color="#fde9b4"/>
      </linearGradient>
      <linearGradient id="cake-chocolate" x1="0" y1="0" x2="0" y2="1">
        <stop offset="0" stop-color="#a86a4a"/><stop offset="0.5" stop-color="#5a3526"/><stop offset="1" stop-color="#222"/>
      </linearGradient>
      <linearGradient id="cake-toffee" x1="0" y1="0" x2="0" y2="1">
        <stop offset="0" stop-color="#a05a34"/><stop offset="0.55" stop-color="#c8844e"/><stop offset="1" stop-color="#222"/>
      </linearGradient>
      <linearGradient id="cake-chip" x1="0" y1="0" x2="0" y2="1">
        <stop offset="0" stop-color="#e4d8b6"/><stop offset="0.6" stop-color="#cdbf98"/><stop offset="1" stop-color="#222"/>
      </linearGradient>
      <linearGradient id="cake-cherry" x1="0" y1="0" x2="0" y2="1">
        <stop offset="0" stop-color="#fbf6f0"/><stop offset="0.45" stop-color="#d8202e"/><stop offset="0.7" stop-color="#f3ead2"/><stop offset="1" stop-color="#222"/>
      </linearGradient>
    </defs>

    <polygon class="banner" points="0,372 740,292 740,380 0,470" fill="url(#banner-fade)"/>

    <g class="frame frame-chocolate" transform="translate(183 610)">
      <use href="#burst" transform="scale(1.3)" fill="var(--frame-brown)"/>
      <use href="#burst" transform="scale(1.14)" fill="var(--white)"/>
      <ellipse rx="96" ry="66" fill="url(#cake-chocolate)" role="img" aria-label="Photo of a chocolate cheesecake with white drizzle"/>
    </g>
    <g class="frame frame-toffee" transform="translate(692 598)">
      <use href="#burst" transform="scale(1.3)" fill="var(--frame-peach)"/>
      <use href="#burst" transform="scale(1.14)" fill="var(--white)"/>
      <ellipse rx="96" ry="66" fill="url(#cake-toffee)" role="img" aria-label="Photo of a caramel toffee brownie cheesecake"/>
    </g>
    <g class="frame frame-chip" transform="translate(183 895)">
      <use href="#burst" transform="scale(1.3)" fill="var(--frame-lime)"/>
      <use href="#burst" transform="scale(1.14)" fill="var(--white)"/>
      <ellipse rx="96" ry="66" fill="url(#cake-chip)" role="img" aria-label="Photo of a chocolate chip cheesecake"/>
    </g>
    <g class="frame frame-cherry" transform="translate(680 895)">
      <use href="#burst" transform="scale(1.3)" fill="var(--frame-red)"/>
      <use href="#burst" transform="scale(1.14)" fill="var(--white)"/>
      <ellipse rx="96" ry="66" fill="url(#cake-cherry)" role="img" aria-label="Photo of a cherry-topped cheesecake with whipped cream"/>
    </g>
  </svg>

  <h1 class="brand"><span class="brand-dot"></span>Velvet Crumb</h1>

  <p class="about">Velvet Crumb, LLC is a local cheesecake company based out of Brayfield, Oakhaven. At Velvet Crumb we strive to provide our customers with a food product that satisfies their greatest indulgence. Velvet Crumb takes a particular approach to preparing one of America’s favorite desserts. Cheesecake is beautiful in nature, so we put a greater emphasis on substance. We don’t use a lot of bells and whistles, but we do add enough bold flavors to pleasure everyone’s palate.</p>

  <p class="slogan">Velvet Crumb is simple, made with a complex human need “Love”.</p>

  <p class="banner-text">build your own options, sizes, prices, delivery availability(local only)<br>and objective statement</p>

  <ul class="flavors">
    <li>Apple</li>
    <li>Banana</li>
    <li>Banana Split (baked or not)</li>
    <li>Brownie Banana Split</li>
    <li>Carmel Toffee Brownie</li>
    <li>Cherry</li>
    <li>Chocolate</li>
    <li>Chocolate Chip</li>
    <li>Cookie Dough</li>
    <li>Cookies &amp; Cream</li>
    <li>Citrus</li>
    <li>Maple Bacon</li>
    <li>Peanut Butter</li>
    <li>Peanut Butter Brownie</li>
    <li>Peanut Butter Pretzel</li>
    <li>Lemon Blueberry</li>
    <li>Strawberry Shortcake</li>
    <li>Smores</li>
    <li>Sweet Potato</li>
    <li>White Chocolate</li>
    <li>Raspberry</li>
  </ul>

  <p class="contact">
    <span class="contact-web">www.tryvelvetcrumb.example</span>
    <span class="contact-email">marna@tryvelvetcrumb.example</span>
  </p>
</main>
</body>
</html>
```